依頼詳細
商品名は「WHEY PROTEIN ISOLATE」です。一般的なプロテインよりも脂肪・糖質を極力排除しており、高純度のたんぱく質を摂取でき、効率的に引き締まった体を作れるのが特徴になります。

メインユーザーは30~40代。男女比はほぼ1:1です。

現行のものは栄養士またはトレーナーがカウンセリングしてから提供することを想定して、名前・量・飲み方を記載して提供できるようにしています(添付ファイルをご覧下さいませ)。レイアウトやデザインは変えてもいいですが、これらの項目自体は変えないようにお願いいたします。

現行品のシンプルさ・清潔感を保ちつつも、「プレミアム」な印象を持てるものになると嬉しいです。

<例1(フォルテン)>
http://shop.forten.jp/products/list.php?category_id=7
<例2(ネクサリオン)>
https://www.nexarion.jp/sports-nutrition/solid-core-blend/48271605.html

以上、よいご提案をお待ちしております。
ご不明な点がございましたら、お気軽にお問い合せ下さいませ。
記載項目
スタンドアルミパウチ:横218mm×縦340mm(チャック下310mm)
※現行品はシールに印刷して貼っていますが、リニューアル品はパウチに印刷しますので、印刷範囲の指定はございません。
希望イメージ
シンプル 複雑
単色 カラフル
暗い 明るい
日常 高級
遊び心 厳粛
未来的 伝統的
女性的 男性的
希望する色
カラーは白地にエメラルドグリーン(DIC63)でお願いいたします。他の色を追加してもOKです。
納品ファイル
• イラストレーター形式 (.ai)
補足説明
選定後はアウトライン化されているファイルと、されていないファイルの両方をお送り下さい。
パーソナルジムに陳列するプロテインですので…あまりにエステっぽいといいますか、女性的なデザインは好ましくないかと思います。
重ねて申し上げますが、シンプルにお願いいたします。<例>もよくご覧下さいませ。
■ 選んだ理由

他にもいいご提案があり悩みましたが、インストラクション部分のデザインが見やすい点が決め手になりました。

■ 提案者全員のお礼・コメント

たくさんのご提案ありがとうございました。また機会がありましたらぜひよろしくお願い致します。

```html
<!DOCTYPE html>
<html lang="en">
<head>
<meta charset="utf-8">
<title>Whey Protein Isolate — Pouch Label</title>
<link rel="stylesheet" href="https://fonts.googleapis.com/css2?family=Comfortaa:wght@500;700&family=Montserrat:wght@400;500;600;700&family=Pacifico&display=swap">
<style>
  :root {
    --emerald: #3fb98a;
    --emerald-deep: #2ea679;
    --charcoal: #4a4b4d;
    --ink: #5a5b5e;
    --mute: #8d8f92;
    --rule: #c9cbcd;
    --paper: #ffffff;
  }
  * { box-sizing: border-box; margin: 0; padding: 0; }
  html, body { width: 818px; height: 1200px; overflow: hidden; background: var(--paper); }
  body { font-family: "Montserrat", Arial, sans-serif; color: var(--ink); }

  .label { position: relative; width: 818px; height: 1200px; background: var(--paper); overflow: hidden; }

  .top-band {
    position: absolute; left: 0; top: 0; width: 100%; height: 52px;
    background: var(--emerald);
    display: flex; align-items: center; justify-content: center;
  }
  .top-band__text { color: #fff; font-size: 13px; letter-spacing: 3px; font-weight: 500; }
  .top-band__rule { position: absolute; left: 0; right: 0; bottom: 8px; height: 1px; background: rgba(255,255,255,.55); }

  .open-note { position: absolute; right: 28px; top: 64px; font-size: 9px; color: var(--mute); }

  .backdrop {
    position: absolute; left: 0; top: 400px; width: 100%; height: 680px;
    background: radial-gradient(ellipse at 60% 45%, #f1f2f3 0%, #f8f8f9 45%, #ffffff 75%);
  }

  .title { position: absolute; left: 0; width: 100%; text-align: center; }
  .title__word {
    display: block; font-family: "Comfortaa", sans-serif; font-weight: 700;
    color: var(--emerald); line-height: 1; letter-spacing: 2px;
  }
  .title__word--whey { position: absolute; top: 170px; left: 0; width: 100%; font-size: 128px; }
  .title__word--protein { position: absolute; top: 272px; left: 0; width: 100%; font-size: 112px; }
  .title__script {
    position: absolute; top: 372px; left: 0; width: 100%;
    font-family: "Pacifico", cursive; font-size: 78px; color: var(--charcoal); line-height: 1.2;
  }

  .tagline { position: absolute; left: 150px; top: 520px; display: flex; gap: 14px; align-items: flex-start; }
  .tagline__mark { width: 48px; height: 48px; flex: none; }
  .tagline__text { font-size: 14px; line-height: 21px; color: var(--ink); padding-top: 4px; }

  .base-band { position: absolute; left: 0; bottom: 0; width: 100%; height: 140px; background: var(--charcoal); }
  .base-band__accent { position: absolute; left: 0; top: 0; width: 100%; height: 3px; background: var(--emerald); }
  .brand {
    position: absolute; left: 0; bottom: 26px; width: 100%;
    display: flex; align-items: center; justify-content: center; gap: 10px;
  }
  .brand__dot { width: 14px; height: 14px; border-radius: 50%; background: var(--emerald); }
  .brand__name { color: var(--emerald); font-family: "Montserrat", sans-serif; font-weight: 700; font-size: 26px; letter-spacing: 4px; }

  .instruction {
    position: absolute; left: 150px; top: 835px; width: 526px; height: 272px;
    background: var(--paper); border-radius: 4px;
    box-shadow: 0 2px 10px rgba(0,0,0,.18);
  }
  .instruction__tab {
    position: absolute; left: 12px; top: -14px; width: 138px; height: 52px;
    background: var(--charcoal); color: #fff; border-radius: 3px 3px 0 0;
    display: flex; flex-direction: column; align-items: center; justify-content: center;
    font-size: 11px; font-weight: 700; letter-spacing: 1px; line-height: 14px;
  }
  .instruction__tab small { font-weight: 500; font-size: 10px; letter-spacing: .5px; }
  .instruction__lead { position: absolute; left: 166px; top: 10px; width: 340px; font-size: 9.5px; line-height: 13px; color: var(--ink); }

  .field-label { font-size: 9.5px; color: var(--ink); border-bottom: 1px solid var(--rule); padding-bottom: 3px; margin-bottom: 8px; }
  .col { position: absolute; width: 225px; }
  .col--left { left: 14px; }
  .col--right { left: 276px; }
  .name-box { width: 225px; height: 36px; border: 1px solid var(--rule); }
  .option { font-size: 11px; color: var(--ink); display: flex; align-items: center; gap: 6px; margin-bottom: 6px; letter-spacing: .5px; }
  .box { width: 10px; height: 10px; border: 1px solid var(--mute); flex: none; }
  .inline-options { display: flex; gap: 14px; }
  .paren { display: inline-flex; width: 150px; justify-content: space-between; }
  .supervised { position: absolute; right: 26px; bottom: 16px; display: flex; align-items: flex-end; gap: 8px; font-size: 9.5px; }
  .supervised__line { width: 210px; border-bottom: 1px solid var(--rule); height: 12px; }
</style>
</head>
<body>
<main class="label">
  <div class="top-band">
    <span class="top-band__text">NUTRITION FOR THE ATHLETE</span>
    <span class="top-band__rule"></span>
  </div>
  <p class="open-note">Cut this line to open</p>

  <div class="backdrop" role="img" aria-label="Faint geometric network line pattern"></div>

  <h1 class="title">
    <span class="title__word title__word--whey">WHEY</span>
    <span class="title__word title__word--protein">PROTEIN</span>
    <span class="title__script">isolate</span>
  </h1>

  <div class="tagline">
    <svg class="tagline__mark" viewBox="0 0 48 48" aria-hidden="true">
      <circle cx="24" cy="24" r="12" fill="var(--emerald)"/>
    </svg>
    <p class="tagline__text">The future of you is built from what you eat today.<br>The only way to realize your dream is to keep taking one small step at a time.</p>
  </div>

  <div class="base-band"><span class="base-band__accent"></span>
    <div class="brand"><span class="brand__dot"></span><span class="brand__name">VERANOVA</span></div>
  </div>

  <section class="instruction">
    <div class="instruction__tab">INSTRUCTION<small>of TRAINER</small></div>
    <p class="instruction__lead">When there are other instructions or precautions of your personal trainer to take this supplement. Please follow them too.</p>

    <div class="col col--left" style="top:52px">
      <p class="field-label">Name of trainer</p>
      <div class="name-box"></div>
    </div>
    <div class="col col--right" style="top:52px">
      <p class="field-label">Drink with</p>
      <div class="inline-options">
        <span class="option"><span class="box"></span>WATER</span>
        <span class="option"><span class="box"></span>MILK</span>
        <span class="option"><span class="box"></span>(&nbsp;&nbsp;&nbsp;&nbsp;&nbsp;&nbsp;)</span>
      </div>
    </div>

    <div class="col col--left" style="top:120px">
      <p class="field-label">Recommended intake per once</p>
      <p class="option"><span class="box"></span>2 SPOON ／ 200cc</p>
      <p class="option"><span class="box"></span>3 SPOON ／ 300cc</p>
      <p class="option"><span class="box"></span>4 SPOON ／ 400cc</p>
      <p class="option"><span class="box"></span><span class="paren"><span>(</span><span>)</span></span></p>
    </div>
    <div class="col col--right" style="top:120px">
      <p class="field-label">Recommended intake timing</p>
      <p class="option"><span class="box"></span>BREAKFAST</p>
      <p class="option"><span class="box"></span>AFTER EXERCIZE</p>
      <p class="option"><span class="box"></span>BEFORE SLEEP</p>
      <p class="option"><span class="box"></span><span class="paren"><span>(</span><span>)</span></span></p>
    </div>

    <div class="supervised"><span>Supervised by</span><span class="supervised__line"></span></div>
  </section>
</main>
</body>
</html>
```